Business Card *

A business card design
Use the logo uploaded in the brief page.
You may use placeholders in your design layouts.
I will provide the actual business card details to the winning designer.

Logo
Place for contact info (name, title, phone, email, etc)

Requirements
Must have
• Logo

```html
<!DOCTYPE html>
<html lang="en">
<head>
<meta charset="utf-8">
<title>Northfield Agriculture and Industry – Business Card</title>
<link href="https://fonts.googleapis.com/css2?family=Roboto:wght@400;700;900&display=swap" rel="stylesheet">
<style>
  :root {
    --page-bg: #e6e6e6;
    --card-white: #ffffff;
    --card-grey: #8f9093;
    --brand-green: #3bb54a;
    --text-grey: #8a8a8a;
    --rule-grey: #bdbdbd;
    --logo-grey: #7b7c7f;
    --emboss-grey: #a2a3a6;
  }
  * { box-sizing: border-box; margin: 0; padding: 0; }
  html, body { width: 1200px; height: 1124px; overflow: hidden; }
  body {
    background: var(--page-bg);
    font-family: "Roboto", Arial, sans-serif;
    position: relative;
  }
  .card {
    position: absolute;
    left: 150px;
    width: 900px;
    height: 500px;
    box-shadow: 0 10px 24px rgba(0,0,0,0.25);
  }
  .card--front {
    top: 40px;
    background: var(--card-white);
    border-bottom: 6px solid var(--brand-green);
  }
  .card--back {
    top: 584px;
    background: var(--card-grey);
    border-left: 6px solid var(--brand-green);
    border-bottom: 6px solid var(--brand-green);
  }

  /* front */
  .brand {
    position: absolute;
    left: 70px;
    top: 180px;
    width: 370px;
    text-align: center;
  }
  .brand__mark {
    display: block;
    width: 70px;
    height: 70px;
    margin: 0 auto 18px;
    border-radius: 50%;
    background: var(--brand-green);
  }
  .brand__name {
    font-weight: 900;
    font-size: 44px;
    letter-spacing: 1px;
    color: var(--logo-grey);
    line-height: 1;
  }
  .brand__tagline {
    margin-top: 8px;
    font-weight: 900;
    font-size: 15px;
    letter-spacing: 2.5px;
    color: var(--logo-grey);
  }
  .divider {
    position: absolute;
    left: 480px;
    top: 110px;
    width: 2px;
    height: 250px;
    background: var(--rule-grey);
  }
  .contact {
    position: absolute;
    left: 520px;
    top: 112px;
    color: var(--text-grey);
  }
  .contact__name {
    font-size: 30px;
    font-weight: 700;
    color: var(--brand-green);
  }
  .contact__title {
    font-size: 22px;
    margin-top: 2px;
  }
  .contact__address {
    font-size: 20px;
    line-height: 1.3;
    margin-top: 18px;
  }
  .contact__list {
    list-style: none;
    margin-top: 18px;
    font-size: 20px;
    line-height: 1.55;
  }
  .contact__list li { display: flex; align-items: center; gap: 12px; }
  .contact__list svg { width: 18px; height: 18px; flex: none; }
  .contact__web-domain { color: var(--brand-green); }

  /* back */
  .back-brand {
    position: absolute;
    left: 0;
    right: 0;
    top: 150px;
    text-align: center;
    color: var(--emboss-grey);
  }
  .back-brand__mark {
    display: block;
    width: 90px;
    height: 90px;
    margin: 0 auto 20px;
    border-radius: 50%;
    background: var(--emboss-grey);
  }
  .back-brand__name {
    font-weight: 900;
    font-size: 58px;
    letter-spacing: 1px;
    line-height: 1;
  }
  .back-brand__tagline {
    margin-top: 6px;
    font-weight: 900;
    font-size: 19px;
    letter-spacing: 3px;
  }
  .back-web {
    position: absolute;
    left: 0;
    right: 0;
    bottom: 40px;
    text-align: center;
    color: #ffffff;
    font-size: 24px;
  }
</style>
</head>
<body>
  <section class="card card--front">
    <div class="brand">
      <span class="brand__mark"></span>
      <div class="brand__name">NORTHFIELD</div>
      <div class="brand__tagline">AGRICULTURE AND INDUSTRY</div>
    </div>
    <div class="divider"></div>
    <div class="contact">
      <div class="contact__name">Daniel Hart</div>
      <div class="contact__title">Manager</div>
      <div class="contact__address">Your address, city<br>state, ZIP 0000</div>
      <ul class="contact__list">
        <li>
          <svg viewBox="0 0 24 24" aria-hidden="true"><path fill="#3bb54a" d="M6.6 10.8a15.1 15.1 0 0 0 6.6 6.6l2.2-2.2a1 1 0 0 1 1-.25 11.4 11.4 0 0 0 3.6.57 1 1 0 0 1 1 1V20a1 1 0 0 1-1 1A17 17 0 0 1 3 4a1 1 0 0 1 1-1h3.5a1 1 0 0 1 1 1c0 1.25.2 2.45.57 3.57a1 1 0 0 1-.25 1z"/></svg>
          555-013-7480
        </li>
        <li>
          <svg viewBox="0 0 24 24" aria-hidden="true"><rect x="3" y="5" width="18" height="14" fill="none" stroke="#3bb54a" stroke-width="2"/><path d="M3 6l9 7 9-7" fill="none" stroke="#3bb54a" stroke-width="2"/></svg>
          youremail@example.com
        </li>
        <li>
          <svg viewBox="0 0 24 24" aria-hidden="true"><circle cx="12" cy="12" r="9" fill="none" stroke="#3bb54a" stroke-width="2"/><path d="M3 12h18M12 3c3 3 3 15 0 18M12 3c-3 3-3 15 0 18" fill="none" stroke="#3bb54a" stroke-width="1.6"/></svg>
          <span>www.<span class="contact__web-domain">yourwebsite</span>.com</span>
        </li>
      </ul>
    </div>
  </section>

  <section class="card card--back">
    <div class="back-brand">
      <span class="back-brand__mark"></span>
      <div class="back-brand__name">NORTHFIELD</div>
      <div class="back-brand__tagline">AGRICULTURE AND INDUSTRY</div>
    </div>
    <div class="back-web">www.yourwebsite.com</div>
  </section>
</body>
</html>
```